2016 Calendar

12 months illustration around a provided grid (template attached) for a 2016 Family Organiser. I would like a concept developed and 2 month samples of that concept submitted for consideration. I would want the project completed in a 1 month time frame. They need to be done in InDesign. So my graphic artist can extract illustration etc to do the front and back covers and import holidays. The 2014 calendar designs can be seen at our webpage www.brightplanners7.com.au and I have attached files of our 3 x 2015 designs to give you a broader idea of what we do currently. Friendly, feel good illustrations that families can relate to and I love humour, so if the illustration makes one smile or laugh, even better, but not necessary. I normally include a quote, but are happy to look at other ideas that might appeal, if you have some fun facts etc. If the graphic artist isn't able to come up with quotes I am happy to find these to compliment the illustration, but space must be left for a quote to go in.

```html
<!DOCTYPE html>
<html lang="en">
<head>
<meta charset="utf-8">
<title>Bright Planners 2016 Family Organiser – Month Samples</title>
<link rel="stylesheet" href="https://fonts.googleapis.com/css2?family=Cookie&family=Comic+Neue:wght@400&display=swap">
<style>
  :root {
    --page-bg: #ffffff;
    --august-band: #8798cb;
    --august-title: #ffff00;
    --november-band: #a2cc44;
    --november-title: #a30fcf;
    --quote-text: #ffffff;
    --art-august: #c9b28f;
    --art-august-soft: #e6dccb;
    --art-november: #f5dfb0;
    --art-november-soft: #e88a4f;
  }
  * { margin: 0; padding: 0; box-sizing: border-box; }
  html, body {
    width: 1161px;
    height: 1200px;
    overflow: hidden;
    background: var(--page-bg);
  }
  .sheet {
    position: relative;
    width: 1161px;
    height: 1200px;
  }
  .month-band {
    position: absolute;
    left: 0;
    width: 1161px;
    height: 410px;
  }
  .month-band--august { top: 155px; background: var(--august-band); }
  .month-band--november { top: 585px; background: var(--november-band); }

  .month-title {
    position: absolute;
    font-family: "Cookie", cursive;
    font-weight: 400;
    font-size: 172px;
    line-height: 1;
    white-space: nowrap;
  }
  .month-band--august .month-title {
    left: 177px;
    top: 112px;
    color: var(--august-title);
  }
  .month-band--november .month-title {
    left: 470px;
    top: 102px;
    color: var(--november-title);
  }

  .month-quote {
    position: absolute;
    font-family: "Comic Neue", cursive;
    font-size: 27px;
    line-height: 33.5px;
    color: var(--quote-text);
    white-space: nowrap;
  }
  .month-band--august .month-quote { left: 414px; top: 260px; }
  .month-band--november .month-quote { left: 541px; top: 273px; }

  .month-art {
    position: absolute;
    display: block;
  }
  .month-art--august { left: 760px; top: 82px; width: 252px; height: 312px; }
  .month-art--november { left: 67px; top: 103px; width: 392px; height: 288px; }
</style>
</head>
<body>
<main class="sheet">
  <section class="month-band month-band--august">
    <h2 class="month-title">August</h2>
    <p class="month-quote">I thought air was free,<br>until I purchased<br>a packet of CHIPS !!</p>
    <svg class="month-art month-art--august" viewBox="0 0 252 312" role="img" aria-label="Illustration: a young man in a cap and jacket holding up a packet of chips beside a grinning blond boy">
      <defs>
        <linearGradient id="august-art-fill" x1="0" y1="0" x2="0" y2="1">
          <stop offset="0" stop-color="var(--art-august-soft)"/>
          <stop offset="1" stop-color="var(--art-august)"/>
        </linearGradient>
      </defs>
      <rect x="0" y="0" width="252" height="312" rx="18" fill="url(#august-art-fill)" opacity="0.85"/>
    </svg>
  </section>

  <section class="month-band month-band--november">
    <svg class="month-art month-art--november" viewBox="0 0 392 288" role="img" aria-label="Illustration: a cheerful man and a small boy waiting beside a wooden bus stop sign">
      <defs>
        <radialGradient id="november-art-fill" cx="0.5" cy="0.5" r="0.6">
          <stop offset="0" stop-color="var(--art-november)"/>
          <stop offset="1" stop-color="var(--art-november-soft)"/>
        </radialGradient>
      </defs>
      <ellipse cx="196" cy="144" rx="196" ry="144" fill="url(#november-art-fill)"/>
    </svg>
    <h2 class="month-title">November</h2>
    <p class="month-quote">When you are waiting for the bus and<br>someone asks, “Has the bus come yet ?”.<br>If the bus came would I be standing here?</p>
  </section>
</main>
</body>
</html>
```